Powerpoint template for trainer and coach in the field of personality development

Powerpoint template for coach and coach in the field of personality development I would like to have a basic design for Powerpoint 2007. It should work: clear, friendly, aesthetic, modern, simple, simple, beautiful, unique, at the same time warm and emotional ("masculine" in the settings seems to lead to rather cool designs). It's about aspects of personality development, psychology, human behavior, which of course has a lot to do with feelings. The lecture, which is based on the presentation, will also be more emotionally colored with objective background than the other. This personal level must be able to transport the design without being too flowery or playful or childish. (I know, maybe it's difficult :-) Charts and statistics are rather rare I would like a basic design for Powerpoint 2007. It should work: clear, friendly, friendly, aesthetic, modern, simple, simple, beautiful, clear, warm and emotional at the same time ("masculine" in the settings seems to lead to rather cool designs). It is about aspects of personality development, psychology and human behavior, which has a lot to do with feelings. So the presentation, which is based on the presentation, wants to be more emotionally colored with a factual background than the other way around. This personal level must be able to transport the design without appearing too flowery or playful or childlike. (I know, it may be difficult: -) Charts and statistics are rather rare Please refer to my previous CI: Logo Website: klaus-muecke. de Workshop-Flyer White as a background colored (red) bar top logo below small would be possible But I can imagine color as a basic background Make suggestions to your taste please and can not be restricted by my ideas The information on the color comes from mine previous agency, I hope you agree. In principle, elements can also be used in the following order: Word document template for handout - seminar materials or offer. Please contact me if you have any questions Best regards I would like a basic design for Powerpoint 2007. It should work: clear, friendly, aesthetic, modern, simple, simple, beautiful, clear Please refer to my previous CI: logo Website: klaus- Mücke. de workshop flyer White background (red) bar at the top of the page. Can you make a color change? The information on the color comes from my previous agency, I hope they are correct. In principle, elements can also be used in the following order: Word document template for handout - seminar materials or offer. With kind regards Color: Red CMYK: 15% Cyan 100% Magenta 100% Yellow 0% Black RGB Dec: 204, 7, 30 RGB%: 80 - 2.7 - 11.8

Target Market(s)

Personnel Developers - Managers -. Employees of companies Also from social enterprises and NGO Personnel developers - executives -. corporate employees So from social enterprises and NGOs

Font styles to use
Sans Serif

Colors
ec1f27

Requirements
Must have
• Title page incl. Logo content page text only: headline plus list No long texts. Only incrustations of max. 7 Punkte = Zeilen Content page Foto, beside Text (Aufzählung) Content page: Foto groß, on which several words as text Title page incl. Logo Content page only text: heading plus enumeration No long texts. Only enumerations of max. 7 points = lines Content page photo, next to it text (list) Contents page: photo large, on it several words as text
Nice to have
• Final page incl. QR code Final page including QR code
Should not have
• playfulness, very technical, cold, empirically oriented playful, very technical, cold, empirically oriented

```html
<!DOCTYPE html>
<html lang="en">
<head>
<meta charset="utf-8">
<title>Klaus Muecke – Presentation Template Overview</title>
<link href="https://fonts.googleapis.com/css2?family=Arimo:wght@400;700&display=swap" rel="stylesheet">
<style>
:root{
  --red:#d21f2d;
  --pink:#e5167f;
  --cyan:#1ba9e2;
  --dark:#2b2b2b;
  --ink:#333333;
  --grey:#8a8a8a;
  --line:#dddddd;
  --row:#fbe4e6;
  --paper:#ffffff;
}
*{box-sizing:border-box;margin:0;padding:0}
html,body{width:1043px;height:1200px;overflow:hidden;background:var(--paper)}
body{font-family:"Arimo",Arial,sans-serif;color:var(--ink)}
h2,h4{font-weight:400}
.sheet{display:grid;grid-template-columns:repeat(3,341px);grid-template-rows:repeat(6,191px);gap:10px 10px;padding-top:2px}
.slide{position:relative;background:var(--paper);overflow:hidden;box-shadow:0 0 0 .5px #e6e6e6}
.abs{position:absolute}
.slide-title{position:absolute;left:17px;top:11px;font-size:11.5px;font-weight:400;letter-spacing:.2px;color:var(--ink);text-transform:uppercase}
.slide-title::after{content:"";position:absolute;left:0;top:19px;width:22px;height:1.5px;background:var(--red)}
.brand{position:absolute;right:10px;top:11px;font-size:7px;font-weight:400;color:var(--ink)}
.footer{position:absolute;left:0;right:0;bottom:0;height:9px;background:var(--red);color:#fff;font-size:3.6px;line-height:9px;padding-left:14px}
.page-no{position:absolute;right:12px;top:0;width:16px;height:9px;background:var(--dark);text-align:center}
.fine{font-size:4px;line-height:1.4;color:var(--grey)}
.fine-white{font-size:4px;line-height:1.45;color:#fff}
.photo{position:absolute}

/* about */
.about-photo{left:0;top:0;width:168px;height:191px;background:linear-gradient(160deg,#c9cdd0,#6f757a 55%,#3f4347)}
.about-box{left:172px;top:48px;width:169px;height:104px;background:var(--red);padding:18px 12px 0 12px}
.about-box h2{font-size:11px;color:#fff;margin-bottom:6px}
.about-box p{margin-bottom:5px}

/* dividers */
.divider-dark{left:0;top:0;width:341px;height:191px;background:linear-gradient(135deg,#5a5a5a,#2f2f2f 60%,#454545)}
.divider-title{position:absolute;left:0;right:0;text-align:center;font-size:18px;font-weight:700;color:#fff}
.divider-sub{position:absolute;font-size:5.5px;color:#fff}
.corner-brand{position:absolute;font-size:8px;font-weight:400;color:var(--ink)}
.divider-red{left:0;top:0;width:341px;height:191px;background:linear-gradient(135deg,#d8303c,#c81f2c 60%,#d63340)}

/* quote */
.quote-box{left:0;top:42px;width:170px;height:121px;background:var(--red);padding:28px 14px 0 14px;color:#fff;font-size:6.8px;line-height:1.35}
.quote-box .author{margin-top:8px}
.quote-photo{left:170px;top:42px;width:171px;height:121px;background:linear-gradient(150deg,#6f8a3a,#3f5a24 50%,#8a6a43)}

/* brand tiles */
.beach{left:25px;top:51px;width:157px;height:108px;background:linear-gradient(180deg,#cfd3d4,#a79b8a 55%,#8c7d6b)}
.tile{position:absolute;width:75px;height:55px;padding:14px 5px 0;text-align:center;color:#fff}
.tile b{display:block;font-size:4.6px;margin-bottom:2px}
.tile span{font-size:3.6px;line-height:1.35;display:block}

/* philosophy */
.feature{position:absolute;width:90px}
.feature h4{font-size:4.8px;margin-bottom:2px}
.ico{position:absolute;border-radius:50%;width:22px;height:22px}

/* bars */
.chart-bg{left:0;top:0;width:341px;height:136px;background:linear-gradient(180deg,#eeeeee,#f7f7f7 60%,#ececec)}
.chart-band{left:0;top:136px;width:341px;height:46px;background:var(--pink)}
.band-col{position:absolute;top:6px;width:80px;text-align:center;color:#fff;line-height:1}
.band-col b{display:block;font-size:5px;margin-bottom:3px}
.band-col span{display:block;font-size:3.6px;line-height:1.4;padding:0 6px}

/* trending */
.map{left:20px;top:48px;width:190px;height:118px;background:radial-gradient(ellipse at 50% 50%,#c6c6c6,#dadada 70%,transparent 72%)}
.stat{position:absolute;border-radius:50%;color:#fff;display:flex;align-items:center;justify-content:center}
.trend-item{position:absolute;left:232px;width:100px}
.trend-item h4{font-size:5px;margin-bottom:1px}
.ring{position:absolute;left:-25px;top:0;width:18px;height:18px;border-radius:50%;border:1.2px solid var(--red)}

/* vision */
.vision-bg{left:0;top:42px;width:341px;height:140px;background:linear-gradient(160deg,#4a4a4a,#2a2a2a 55%,#3b3b3b)}
.vision{position:absolute;color:#fff}
.mission-dot{position:absolute;width:10px;height:10px;border-radius:50%;background:#fff}

/* services */
.swim{left:30px;top:42px;width:128px;height:70px;background:linear-gradient(160deg,#5d7d8c,#3e5a66 55%,#8a7966)}
.svc{position:absolute;left:178px;width:150px}
.svc h4{font-size:5.6px;margin-bottom:1px}
.svc-ico{position:absolute;left:-18px;top:0;width:11px;height:11px;border-radius:50%}

/* columns */
.lead{left:20px;top:46px;width:250px;font-size:6.4px;line-height:1.35;color:var(--red)}
.col{position:absolute;top:76px;width:86px}
.col p{margin-bottom:6px}

/* team */
.portrait{left:127px;top:39px;width:84px;height:84px;border-radius:50%;background:linear-gradient(160deg,#b7babd,#6b7075 60%,#4a4e52)}
.social{position:absolute;top:162px;width:4.5px;height:4.5px;border-radius:50%;background:var(--pink)}

/* pricing */
.price-band{left:0;top:80px;width:341px;height:102px;background:var(--red)}
.card{position:absolute;background:#fff;box-shadow:0 1px 2px rgba(0,0,0,.2)}
.card-head{color:#fff;text-align:center;padding-top:5px;line-height:1}
.card-head .amt{font-size:12px}
.card-head .amt sup{font-size:6px}
.card-head small{display:block;font-size:3.5px;margin-top:1px}
.card li{list-style:none;font-size:3.6px;color:var(--grey);text-align:center;border-bottom:.5px solid var(--line);padding:3.2px 0}

/* table */
.data{position:absolute;left:22px;top:44px;width:300px;border-collapse:collapse;font-size:3.8px}
.data th{background:var(--red);color:#fff;font-weight:400;height:9px}
.data td{height:8.6px;text-align:center;color:#777;border-bottom:.5px solid #f1c4c8}
.data tr:nth-child(odd) td{background:var(--row)}
.data td:first-child{text-align:left;padding-left:8px;color:var(--red)}

/* team four */
.member{position:absolute;width:140px}
.avatar{position:absolute;left:0;top:0;width:34px;height:34px;border-radius:50%;background:#c9c9c9}
.member .info{position:absolute;left:40px;top:0;width:100px}
.member h4{font-size:6px;color:var(--pink)}
.member .role{font-size:3.8px;color:var(--ink)}
.member ul{margin-top:2px;padding-left:6px}
.member li{font-size:3.4px;color:var(--grey);line-height:1.35}

/* testimonials */
.test-photo{left:74px;top:42px;width:44px;height:44px;border-radius:50%;background:linear-gradient(160deg,#b7babd,#6b7075 60%,#4a4e52)}
.test-band{left:0;top:98px;width:341px;height:84px;background:var(--red)}
.test-icon{position:absolute;top:115px;width:22px;height:22px;border-radius:50%;border:1px solid #fff}
.test-cap{position:absolute;top:142px;width:54px;text-align:center}

/* pictures */
.water{left:25px;top:38px;width:138px;height:140px;background:linear-gradient(170deg,#5d6463,#2d3130 50%,#6b7272)}
.leaves{left:167px;top:38px;width:138px;height:140px;background:linear-gradient(160deg,#6d7a3a,#5a4a30 55%,#8a6a45)}
.mud{left:24px;top:38px;width:292px;height:74px;background:linear-gradient(170deg,#9aa0a0,#7a6a55 55%,#5c4d3b)}
.red-lead{left:24px;top:117px;width:138px;font-size:6px;line-height:1.35;color:var(--red)}
</style>
</head>
<body>
<main class="sheet">

<section class="slide">
  <div class="photo about-photo" role="img" aria-label="Portrait of a grey-haired coach in a grey suit, gesturing while speaking"></div>
  <div class="abs about-box">
    <h2>ABOUT US</h2>
    <p class="fine-white">Lorem ipsum dolor sit amet, consectetur adipiscing elit, sed do eiusmod tempor incididunt ut labore et dolore magna aliqua.</p>
    <p class="fine-white">Ut enimad minim veniam, quis nostrud exercitation ullamco laboris nisi ut aliquip ex ea commodo consequat.</p>
  </div>
</section>

<section class="slide">
  <div class="photo divider-dark" role="img" aria-label="Dark monochrome photo of people in a workshop"></div>
  <h2 class="divider-title" style="top:78px">THIS IS YOUR DIVIDER PAGE</h2>
  <p class="divider-sub" style="left:192px;top:101px">YOUR SUBTITLE GOES HERE</p>
  <svg class="abs" style="left:0;top:0" width="341" height="191" viewBox="0 0 341 191"><polygon points="341,112 341,191 220,191" fill="#fff"/></svg>
  <span class="corner-brand" style="right:12px;top:172px">Klaus Muecke</span>
</section>

<section class="slide">
  <h2 class="slide-title">Quote Area</h2>
  <span class="brand">Klaus Muecke</span>
  <div class="abs quote-box">
    <p>“ Coming together is a beginning.<br>Keeping together is progress.<br>Working together is success.</p>
    <p class="author">- Hal Brenton - ”</p>
  </div>
  <div class="photo quote-photo" role="img" aria-label="Moss-covered forest floor with trees"></div>
  <div class="footer">© Copyright 2017 Klaus Muecke. All rights reserved.<span class="page-no">03</span></div>
</section>

<section class="slide">
  <h2 class="slide-title">Brand Detailed</h2>
  <span class="brand">Klaus Muecke</span>
  <div class="photo beach" role="img" aria-label="Footprints in the sand on a quiet beach"></div>
  <div class="tile" style="left:185px;top:50px;background:var(--red)"><b>SYSTEM</b><span>Mauris quam dolor, cursus ut porta id, luctus eget purus. Nunc tempor luctus interdum.</span></div>
  <div class="tile" style="left:262px;top:50px;background:var(--dark)"><b>TECHNOLOGY</b><span>Mauris quam dolor, cursus ut porta id, luctus eget purus. Nunc tempor luctus interdum.</span></div>
  <div class="tile" style="left:185px;top:107px;background:var(--pink)"><b>LEISURE</b><span>Mauris quam dolor, cursus ut porta id, luctus eget purus. Nunc tempor luctus interdum.</span></div>
  <div class="tile" style="left:262px;top:107px;background:var(--cyan)"><b>DIGITAL</b><span>Mauris quam dolor, cursus ut porta id, luctus eget purus. Nunc tempor luctus interdum.</span></div>
  <div class="footer">© Copyright 2017 Klaus Muecke. All rights reserved.<span class="page-no">04</span></div>
</section>

<section class="slide">
  <h2 class="slide-title">Product Philosophy</h2>
  <span class="brand">Klaus Muecke</span>
  <div class="feature" style="left:20px;top:52px;text-align:right;width:62px"><h4 style="color:var(--red)">SECURE</h4><p class="fine">Nullam eu tempor purus. Nunc a leo magna, sit amet consequat risus.</p></div>
  <div class="ico" style="left:88px;top:52px;background:var(--red)"></div>
  <div class="feature" style="left:20px;top:126px;text-align:right;width:62px"><h4 style="color:var(--cyan)">GOOD PACKAGE</h4><p class="fine">Nullam eu tempor purus. Nunc a leo magna, sit amet consequat risus.</p></div>
  <div class="ico" style="left:88px;top:126px;background:var(--cyan)"></div>
  <svg class="abs" style="left:118px;top:62px" width="104" height="104" viewBox="0 0 100 100">
    <g transform="rotate(-90 50 50)" fill="none" stroke-width="15">
      <circle cx="50" cy="50" r="32" stroke="#2b2b2b" stroke-dasharray="30.2 201"/>
      <circle cx="50" cy="50" r="32" stroke="#e5167f" stroke-dasharray="50.3 201" stroke-dashoffset="-30.2"/>
      <circle cx="50" cy="50" r="32" stroke="#1ba9e2" stroke-dasharray="40.2 201" stroke-dashoffset="-80.5"/>
      <circle cx="50" cy="50" r="32" stroke="#d21f2d" stroke-dasharray="80.4 201" stroke-dashoffset="-120.7"/>
    </g>
    <circle cx="50" cy="50" r="19" fill="#f2f2f2"/>
    <g font-size="5.5" fill="#fff" text-anchor="middle" font-family="Arimo, Arial, sans-serif">
      <text x="60" y="25">15%</text><text x="82" y="58">25%</text><text x="50" y="86">20%</text><text x="20" y="49">40%</text>
    </g>
  </svg>
  <div class="ico" style="left:229px;top:50px;background:var(--dark)"></div>
  <div class="feature" style="left:256px;top:52px;width:68px"><h4>WELL ORGANIZED</h4><p class="fine">Nullam eu tempor purus. Nunc a leo magna, sit amet consequat risus.</p></div>
  <div class="ico" style="left:229px;top:126px;background:var(--pink)"></div>
  <div class="feature" style="left:256px;top:126px;width:68px"><h4 style="color:var(--pink)">PUBLICATION</h4><p class="fine">Nullam eu tempor purus. Nunc a leo magna, sit amet consequat risus.</p></div>
  <div class="footer">© Copyright 2017 Klaus Muecke. All rights reserved.<span class="page-no">05</span></div>
</section>

<section class="slide">
  <div class="photo chart-bg" role="img" aria-label="Faint light photo of water behind the chart"></div>
  <svg class="abs" style="left:0;top:0" width="341" height="136" viewBox="0 0 341 136" font-family="Arimo, Arial, sans-serif" font-size="6" text-anchor="middle" fill="#2b2b2b">
    <rect x="150" y="20" width="4" height="3" fill="#d21f2d"/><text x="162" y="23" font-size="3.5">2014</text>
    <rect x="172" y="20" width="4" height="3" fill="#2b2b2b"/><text x="184" y="23" font-size="3.5">2015</text>
    <rect x="30" y="73" width="18" height="63" fill="#d21f2d"/><text x="39" y="69">400</text>
    <rect x="53" y="57" width="18" height="79" fill="#2b2b2b"/><text x="62" y="53">500</text>
    <rect x="112" y="89" width="18" height="47" fill="#d21f2d"/><text x="121" y="85">300</text>
    <rect x="135" y="41" width="18" height="95" fill="#2b2b2b"/><text x="144" y="37">600</text>
    <rect x="193" y="90" width="18" height="46" fill="#d21f2d"/><text x="202" y="86">290</text>
    <rect x="216" y="104" width="18" height="32" fill="#2b2b2b"/><text x="225" y="100">200</text>
    <rect x="276" y="104" width="18" height="32" fill="#d21f2d"/><text x="285" y="100">200</text>
    <rect x="299" y="120" width="18" height="16" fill="#2b2b2b"/><text x="308" y="116">100</text>
  </svg>
  <div class="abs chart-band">
    <div class="band-col" style="left:9px"><b>Asia</b><span>Duis quis purus aliquet scelerisque dolor quis vel eros. Nullam eu tempor purus.</span></div>
    <div class="band-col" style="left:91px"><b>Africa</b><span>Duis quis purus aliquet scelerisque dolor quis vel eros. Nullam eu tempor purus.</span></div>
    <div class="band-col" style="left:173px"><b>America</b><span>Duis quis purus aliquet scelerisque dolor quis vel eros. Nullam eu tempor purus.</span></div>
    <div class="band-col" style="left:255px"><b>Euro</b><span>Duis quis purus aliquet scelerisque dolor quis vel eros. Nullam eu tempor purus.</span></div>
  </div>
  <div class="footer">© Copyright 2017 Klaus Muecke. All rights reserved.<span class="page-no">06</span></div>
</section>

<section class="slide">
  <h2 class="slide-title">Trending in the World</h2>
  <span class="brand">Klaus Muecke</span>
  <div class="photo map" role="img" aria-label="Grey world map"></div>
  <div class="stat" style="left:30px;top:110px;width:24px;height:24px;background:var(--red);font-size:7px">25%</div>
  <div class="stat" style="left:92px;top:72px;width:36px;height:36px;background:var(--dark);font-size:11px">80%</div>
  <div class="stat" style="left:186px;top:100px;width:34px;height:34px;background:var(--cyan);font-size:11px">75%</div>
  <div class="stat" style="left:158px;top:130px;width:18px;height:18px;background:var(--pink);font-size:5px">15%</div>
  <div class="trend-item" style="top:56px"><span class="ring"></span><h4 style="color:var(--red)">Confusion</h4><p class="fine">Nullam eu tempor purus. Nunc a leo magna, sit amet consequat risus.</p></div>
  <div class="trend-item" style="top:92px"><span class="ring" style="border-color:var(--dark)"></span><h4>Intangible</h4><p class="fine">Nullam eu tempor purus. Nunc a leo magna, sit amet consequat risus.</p></div>
  <div class="trend-item" style="top:128px"><span class="ring" style="border-color:var(--pink)"></span><h4 style="color:var(--pink)">Performance</h4><p class="fine">Nullam eu tempor purus. Nunc a leo magna, sit amet consequat risus.</p></div>
  <div class="footer">© Copyright 2017 Klaus Muecke. All rights reserved.<span class="page-no">07</span></div>
</section>

<section class="slide">
  <h2 class="slide-title">Our Vision &amp; Mission</h2>
  <span class="brand">Klaus Muecke</span>
  <div class="photo vision-bg" role="img" aria-label="Dark photo of an audience in a seminar room"></div>
  <div class="vision" style="left:18px;top:52px;width:150px">
    <p style="font-size:8px;margin-bottom:5px">▪ Our Vision:</p>
    <p style="font-size:6.2px;font-weight:700;line-height:1.35;margin-bottom:8px">Go to the Next Level<br>Without look in the past</p>
    <p class="fine-white">Lorem ipsum dolor sit amet, consectetur adipiscing elit, sed do eiusmod tempor incididunt ut labore et dolore magna aliqua. Ut enimad minim veniam, quis nostrud exercitation ullamco laboris nisi ut aliquip ex ea commodo consequat.</p>
  </div>
  <div class="vision" style="left:182px;top:52px;width:150px"><p style="font-size:8px">▪ Our Missions:</p></div>
  <span class="mission-dot" style="left:188px;top:69px"></span>
  <div class="vision" style="left:208px;top:68px;width:125px"><p style="font-size:7px">Your Text Here</p><p class="fine-white">Lorem ipsum dolor sit consectetur adipiscing elit, sed do eiusmod tempor.</p></div>
  <span class="mission-dot" style="left:188px;top:94px"></span>
  <div class="vision" style="left:208px;top:93px;width:125px"><p style="font-size:7px">Your Text Here</p><p class="fine-white">Lorem ipsum dolor sit consectetur adipiscing elit, sed do eiusmod tempor.</p></div>
  <span class="mission-dot" style="left:188px;top:119px"></span>
  <div class="vision" style="left:208px;top:118px;width:125px"><p style="font-size:7px">Your Text Here</p><p class="fine-white">Lorem ipsum dolor sit consectetur adipiscing elit, sed do eiusmod tempor.</p></div>
  <div class="footer">© Copyright 2017 Klaus Muecke. All rights reserved.<span class="page-no">08</span></div>
</section>

<section class="slide">
  <h2 class="slide-title">Our Services</h2>
  <span class="brand">Klaus Muecke</span>
  <div class="photo swim" role="img" aria-label="Swimmer resting on a rock by the sea"></div>
  <p class="abs" style="left:30px;top:117px;font-size:5.8px;color:var(--red)">Your Title Goes Here</p>
  <p class="abs fine" style="left:30px;top:125px;width:130px">Lorem ipsum dolor sit amet, sed do eiusmod tempor incididunt ut labore et dolore magna aliqua. Ut enimad minim veniam, quis nostrud exercitation ullamco laboris nisi ut aliquip.</p>
  <div class="svc" style="top:46px"><span class="svc-ico" style="background:var(--red)"></span><h4 style="color:var(--red)">Service Number One</h4><p class="fine">Lorem ipsum dolor sit amet, consectetur adipiscing elit, sed do eiusmod tempor incididunt ut labore et dolore magna aliqua.</p></div>
  <div class="svc" style="top:84px"><span class="svc-ico" style="background:var(--dark)"></span><h4>Service Number Two</h4><p class="fine">Lorem ipsum dolor sit amet, consectetur adipiscing elit, sed do eiusmod tempor incididunt ut labore et dolore magna aliqua.</p></div>
  <div class="svc" style="top:122px"><span class="svc-ico" style="background:var(--pink)"></span><h4 style="color:var(--pink)">Service Number Three</h4><p class="fine">Lorem ipsum dolor sit amet, consectetur adipiscing elit, sed do eiusmod tempor incididunt ut labore et dolore magna aliqua.</p></div>
  <div class="footer">© Copyright 2017 Klaus Muecke. All rights reserved.<span class="page-no">09</span></div>
</section>

<section class="slide">
  <h2 class="slide-title">Three Column Description</h2>
  <span class="brand">Klaus Muecke</span>
  <p class="abs lead">This is place for your header text. Insert your text here, just replace this text with your own text</p>
  <div class="col" style="left:20px"><p class="fine">Lorem ipsum dolor sit amet, consectetur adipiscing elit, sed do eiusmod tempor incididunt ut labore et dolore magna aliqua. Ut enimad minim veniam, quis nostrud exercitation ullamco laboris nisi ut aliquip ex ea commodo consequat.</p><p class="fine">Duis aute irure dolor in reprehenderit in voluptate velit esse cillum dolore eu fugiat nulla pariatur excepteur.</p></div>
  <div class="col" style="left:124px"><p class="fine">Lorem ipsum dolor sit amet, consectetur adipiscing elit, sed do eiusmod tempor incididunt ut labore et dolore magna aliqua. Ut enimad minim veniam, quis nostrud exercitation ullamco laboris nisi ut aliquip ex ea commodo consequat.</p><p class="fine">Duis aute irure dolor in reprehenderit in voluptate velit esse cillum dolore eu fugiat nulla pariatur excepteur.</p></div>
  <div class="col" style="left:228px;border-left:.5px solid var(--line);padding-left:6px"><p class="fine">Lorem ipsum dolor sit amet, consectetur adipiscing elit, sed do eiusmod tempor incididunt ut labore et dolore magna aliqua. Ut enimad minim veniam, quis nostrud exercitation ullamco laboris nisi ut aliquip ex ea commodo consequat.</p><p class="fine">Duis aute irure dolor in reprehenderit in voluptate velit esse cillum dolore eu fugiat nulla pariatur excepteur.</p></div>
  <div class="footer">© Copyright 2017 Klaus Muecke. All rights reserved.<span class="page-no">10</span></div>
</section>

<section class="slide">
  <h2 class="slide-title">Our Team</h2>
  <span class="brand">Klaus Muecke</span>
  <div class="photo portrait" role="img" aria-label="Round portrait of the CEO"></div>
  <p class="abs" style="left:0;right:0;top:129px;text-align:center;font-size:4.6px">Mr. John Smith</p>
  <p class="abs" style="left:0;right:0;top:135px;text-align:center;font-size:4.6px;color:var(--red)">CEO</p>
  <p class="abs fine" style="left:110px;top:142px;width:120px;text-align:center;font-size:3.4px">Lorem ipsum dolor sit amet, consectetur adipiscing elit, sed do eiusmod tempor incididunt ut labore et dolore magna aliqua ut enim.</p>
  <span class="social" style="left:158px"></span><span class="social" style="left:165px"></span><span class="social" style="left:172px"></span><span class="social" style="left:179px"></span>
  <div class="footer">© Copyright 2017 Klaus Muecke. All rights reserved.<span class="page-no">11</span></div>
</section>

<section class="slide">
  <div class="photo divider-red" role="img" aria-label="Red-tinted photo of a kayaker in white water"></div>
  <svg class="abs" style="left:0;top:0" width="341" height="191" viewBox="0 0 341 191"><polygon points="0,0 130,0 0,78" fill="#fff"/></svg>
  <span class="corner-brand" style="left:14px;top:14px">Klaus Muecke</span>
  <h2 class="divider-title" style="top:78px;left:30px">THIS IS YOUR DIVIDER PAGE</h2>
  <p class="divider-sub" style="left:196px;top:101px">YOUR SUBTITLE GOES HERE</p>
</section>

<section class="slide">
  <h2 class="slide-title">Monthly Subscription</h2>
  <span class="brand">Klaus Muecke</span>
  <div class="abs price-band"></div>
  <div class="card" style="left:50px;top:60px;width:64px;height:88px">
    <div class="card-head" style="background:var(--pink);height:24px"><span class="amt"><sup>$</sup>300</span><small>per month</small></div>
    <ul><li>Single Edition</li><li>30gb Cloud Service</li><li>5 User</li><li>Free Update</li></ul>
  </div>
  <div class="card" style="left:123px;top:52px;width:84px;height:103px">
    <div class="card-head" style="background:var(--red);height:28px"><span class="amt" style="font-size:14px"><sup>$</sup>900</span><small>per month</small></div>
    <ul><li>Business Edition</li><li>90gb Cloud Service</li><li>6 User</li><li>Free Update</li></ul>
  </div>
  <div class="card" style="left:216px;top:60px;width:64px;height:88px">
    <div class="card-head" style="background:var(--dark);height:24px"><span class="amt"><sup>$</sup>400</span><small>per month</small></div>
    <ul><li>Single Edition</li><li>40gb Cloud Service</li><li>5 User</li><li>Free Update</li></ul>
  </div>
  <div class="footer">© Copyright 2017 Klaus Muecke. All rights reserved.<span class="page-no">13</span></div>
</section>

<section class="slide">
  <h2 class="slide-title">Your Title Goes Here</h2>
  <span class="brand">Klaus Muecke</span>
  <p class="abs fine" style="left:22px;top:34px;width:230px;font-size:3.4px"><b style="color:var(--ink)">Description</b> There are many variations of passages of lorem ipsum available, but the majority have suffered alteration in some form.</p>
  <table class="data">
    <tr><th>Lorem ipsum</th><th>Value</th><th>Value</th><th>Value</th><th>Value</th></tr>
    <tr><td>Lorem ipsum</td><td>10</td><td>15</td><td>16</td><td>18</td></tr>
    <tr><td>Lorem ipsum</td><td>10</td><td>33</td><td>15</td><td>16</td></tr>
    <tr><td>Lorem ipsum</td><td>20</td><td>22</td><td>23</td><td>25</td></tr>
    <tr><td>Lorem ipsum</td><td>30</td><td>23</td><td>33</td><td>33</td></tr>
    <tr><td>Lorem ipsum</td><td>15</td><td>25</td><td>33</td><td>32</td></tr>
    <tr><td>Lorem ipsum</td><td>30</td><td>02</td><td>33</td><td>25</td></tr>
    <tr><td>Lorem ipsum</td><td>35</td><td>35</td><td>05</td><td>32</td></tr>
    <tr><td>Lorem ipsum</td><td>26</td><td>30</td><td>35</td><td>32</td></tr>
    <tr><td>Lorem ipsum</td><td>32</td><td>30</td><td>32</td><td>32</td></tr>
  </table>
  <div class="footer">© Copyright 2017 Klaus Muecke. All rights reserved.<span class="page-no">14</span></div>
</section>

<section class="slide">
  <h2 class="slide-title">Our Team</h2>
  <span class="brand">Klaus Muecke</span>
  <div class="member" style="left:20px;top:44px"><span class="avatar" role="img" aria-label="Portrait of Michael Doe" style="background:linear-gradient(160deg,#b7babd,#5f6469)"></span><div class="info"><h4>Michael Doe</h4><p class="role">CEO<br>MBA, MBA and CMA Dip PM</p><ul><li>Lorem ipsum dolor sit amet, consectetur adipiscing elit</li><li>sed do eiusmod tempor incididunt ut labore et dolore magna</li><li>Ut enimad minim veniam, quis nostrud</li></ul></div></div>
  <div class="member" style="left:184px;top:44px"><span class="avatar"></span><div class="info"><h4>James Doe</h4><p class="role">Manager<br><span style="color:var(--pink)">M.B.A</span></p><ul><li>Lorem ipsum dolor sit amet, consectetur adipiscing elit</li><li>sed do eiusmod tempor incididunt ut labore et dolore magna</li><li>Ut enimad minim veniam, quis nostrud</li></ul></div></div>
  <div class="member" style="left:20px;top:108px"><span class="avatar"></span><div class="info"><h4>Jane Doe</h4><p class="role">Doctor of Chemistry<br><span style="color:var(--pink)">M.B.A</span></p><ul><li>Lorem ipsum dolor sit amet, consectetur adipiscing elit</li><li>sed do eiusmod tempor incididunt ut labore et dolore magna</li><li>Ut enimad minim veniam, quis nostrud</li></ul></div></div>
  <div class="member" style="left:184px;top:108px"><span class="avatar"></span><div class="info"><h4>John Doe</h4><p class="role">Doctor of Physical<br><span style="color:var(--pink)">Professor</span></p><ul><li>Lorem ipsum dolor sit amet, consectetur adipiscing elit</li><li>sed do eiusmod tempor incididunt ut labore et dolore magna</li><li>Ut enimad minim veniam, quis nostrud</li></ul></div></div>
  <div class="footer">© Copyright 2017 Klaus Muecke. All rights reserved.<span class="page-no">15</span></div>
</section>

<section class="slide">
  <h2 class="slide-title">Customer Testimonials</h2>
  <span class="brand">Klaus Muecke</span>
  <div class="photo test-photo" role="img" aria-label="Round portrait of a client"></div>
  <p class="abs fine" style="left:142px;top:46px;width:170px">adipiscing elit, sed diam nonummy nibh euismod tincidunt ut laoreet dolore magna aliquam erat volutpat. Ut wisi enim <b style="color:var(--red)">Lorem ipsum</b> dolor sit amet, consectetuer adipiscing elit, sed diam nonummy nibh euismod tincidunt ut laoreet dolore magna.</p>
  <div class="abs test-band"></div>
  <svg class="abs" style="left:88px;top:92px" width="14" height="7" viewBox="0 0 14 7"><polygon points="0,6 7,0 14,6 14,7 0,7" fill="#d21f2d"/></svg>
  <span class="test-icon" style="left:68px"></span><span class="test-icon" style="left:129px"></span><span class="test-icon" style="left:190px"></span><span class="test-icon" style="left:251px"></span>
  <p class="test-cap fine-white" style="left:52px;font-size:3.4px">Why does getting a task hand to be so much more complicated than ordering a fridge online?</p>
  <p class="test-cap fine-white" style="left:113px;font-size:3.4px">Why do I have to go to a branch, fill out forms and wait for weeks to get a response?</p>
  <p class="test-cap fine-white" style="left:174px;font-size:3.4px">Why do banks refuse to lend to me despite the consistent flow of my income each month?</p>
  <p class="test-cap fine-white" style="left:235px;font-size:3.4px">Why is there no answer in banking that identifies my needs and offers convenience when I need it?</p>
  <div class="footer">© Copyright 2017 Klaus Muecke. All rights reserved.<span class="page-no">16</span></div>
</section>

<section class="slide">
  <h2 class="slide-title">Two Pictures Slide</h2>
  <span class="brand">Klaus Muecke</span>
  <div class="photo water" role="img" aria-label="Dark rippling water surface"></div>
  <div class="photo leaves" role="img" aria-label="Mossy tree roots with autumn leaves"></div>
  <div class="footer">© Copyright 2017 Klaus Muecke. All rights reserved.<span class="page-no">17</span></div>
</section>

<section class="slide">
  <h2 class="slide-title">Title and Image + Text</h2>
  <span class="brand">Klaus Muecke</span>
  <div class="photo mud" role="img" aria-label="Team of people crawling through mud during an outdoor challenge"></div>
  <p class="abs red-lead">Lorem ipsum dolor sit amet, consectetur adipiscing elit, sed do eiusmod tempor incididunt ut labore et dolore magna aliqua. Ut enimad minim veniam, quis Lorem ipsum dolor sit amet</p>
  <p class="abs fine" style="left:170px;top:117px;width:146px">Lorem ipsum dolor sit amet, consectetur adipiscing elit, sed do eiusmod tempor incididunt ut labore et dolore magna aliqua. Ut enimad minim veniam, quis nostrud exercitation ullamco laboris nisi ut aliquip ex ea commodo consequat.</p>
  <p class="abs fine" style="left:170px;top:146px;width:146px">Duis aute irure dolor in reprehenderit in voluptate velit esse cillum dolore eu fugiat nulla pariatur. Excepteur sint occaecat cupidatat non proident, sunt in culpa qui officia deserunt mollit anim id est laborum.</p>
  <div class="footer">© Copyright 2017 Klaus Muecke. All rights reserved.<span class="page-no">18</span></div>
</section>

</main>
</body>
</html>
```